Business card

would like a double sided business card made up with my logos provided.
Prefer card to have black background and to use the black logos, with matching blue writing for the text.
One side to just be the logo, (Try to use both the black logos)
the other side to have the logo and also my credentials/business information.

Covering all aspects of Carpentry and Building Services

Marcus Tolvey
Qualified Carpenter
Mob: 0417263948
Email: rkt.joinery@mailbright.com
ABN: 47 615 209 834

Industry/Entity Type

Business

Contact Information for Business Card

Marcus Tolvey
Qualified Carpenter
Mob: 0417263948
ABN: 47 615 209 834

Requirements
Must have
• Please try to use both the black logos and incorporate into the card.

```html
<!DOCTYPE html>
<html lang="en">
<head>
<meta charset="utf-8">
<title>RKT Joinery – Business Card</title>
<link rel="stylesheet" href="https://fonts.googleapis.com/css2?family=Montserrat:wght@400;500;600;700&display=swap">
<style>
  :root {
    --backdrop: #2b2b2d;
    --card: #0a101c;
    --card-edge: #131b2b;
    --blue: #2b8fd0;
    --white: #eef1f4;
    --muted: #c9ced6;
  }
  * { box-sizing: border-box; margin: 0; padding: 0; }
  html, body {
    width: 1200px; height: 900px; overflow: hidden;
    background: var(--backdrop);
    font-family: "Montserrat", sans-serif;
  }
  .sheet {
    position: relative; width: 1200px; height: 900px;
    display: flex; flex-direction: column; align-items: center; justify-content: center; gap: 40px;
  }
  .card {
    position: relative; width: 640px; height: 390px;
    background: var(--card);
    border: 1px solid var(--card-edge);
    border-radius: 24px;
    box-shadow: 0 18px 40px rgba(0,0,0,.45);
    overflow: hidden;
  }
  /* Front */
  .card--front { display: flex; align-items: center; justify-content: center; }
  .brand { display: flex; align-items: center; gap: 18px; }
  .brand__mark { width: 34px; height: 34px; background: var(--blue); }
  .brand__name {
    font-weight: 700; color: var(--white); letter-spacing: 3px; text-transform: uppercase;
  }
  .card--front .brand__name { font-size: 52px; }
  /* Back */
  .services {
    position: absolute; left: 46px; top: 120px; width: 220px;
    color: var(--blue); font-weight: 600; font-size: 17px; line-height: 1.3;
  }
  .contact {
    position: absolute; right: 46px; top: 42px; text-align: right;
  }
  .contact__name { color: var(--blue); font-weight: 700; font-size: 20px; letter-spacing: 1.5px; text-transform: uppercase; }
  .contact__role { color: var(--blue); font-weight: 600; font-size: 15px; margin-top: 2px; }
  .contact__abn { color: var(--white); font-weight: 500; font-size: 12px; letter-spacing: .5px; margin-top: 4px; }
  .contact__lines { margin-top: 26px; display: flex; flex-direction: column; gap: 8px; align-items: flex-end; }
  .contact__line { display: flex; align-items: center; gap: 10px; color: var(--white); font-weight: 500; font-size: 16px; letter-spacing: .5px; }
  .contact__icon { width: 20px; height: 20px; border-radius: 5px; background: var(--blue); display: flex; align-items: center; justify-content: center; }
  .card--back .brand { position: absolute; left: 46px; bottom: 52px; }
  .card--back .brand__mark { width: 30px; height: 30px; }
  .card--back .brand__name { font-size: 44px; }
</style>
</head>
<body>
<main class="sheet">
  <section class="card card--front" aria-label="Card front">
    <div class="brand">
      <span class="brand__mark"></span>
      <span class="brand__name">RKT Joinery</span>
    </div>
  </section>

  <section class="card card--back" aria-label="Card back">
    <p class="services">Covering all aspects of Carpentry and Building Services</p>

    <div class="contact">
      <p class="contact__name">Marcus Tolvey</p>
      <p class="contact__role">Qualified Carpenter</p>
      <p class="contact__abn">ABN: 47 615 209 834</p>
      <div class="contact__lines">
        <p class="contact__line">0417 263 948
          <span class="contact__icon">
            <svg width="10" height="14" viewBox="0 0 10 14" aria-hidden="true"><rect x="1" y="1" width="8" height="12" rx="1.5" fill="none" stroke="#fff" stroke-width="1.4"/><circle cx="5" cy="10.5" r=".9" fill="#fff"/></svg>
          </span>
        </p>
        <p class="contact__line">rkt.joinery@mailbright.com
          <span class="contact__icon">
            <svg width="13" height="10" viewBox="0 0 13 10" aria-hidden="true"><rect x=".7" y=".7" width="11.6" height="8.6" rx="1" fill="none" stroke="#fff" stroke-width="1.3"/><path d="M1 1.2 6.5 5.6 12 1.2" fill="none" stroke="#fff" stroke-width="1.3"/></svg>
          </span>
        </p>
      </div>
    </div>

    <div class="brand">
      <span class="brand__mark"></span>
      <span class="brand__name">RKT Joinery</span>
    </div>
  </section>
</main>
</body>
</html>
```